Mergers and Acquisitions Business Seeks Fresh Website Design

IMPORTANT: Please only design the Homepage, for the contest. If you win the contest, you will design the inner pages, as see in the attached document 'Brevka 2025 website wireframes."
Design a new website for Brevka at brevka.global. Maintaining current Impact and Open Sans fonts, or using open-source alternatives from Google Fonts.
Enhance the design with a premium feel, impactful visuals, and dynamic content. We want the new design to focus on generating high-quality inquiries, strong calls to action, and consistent branding.
Industry/Entity Type
Mergers and Acquisitions
Number of Pages Required
5+ page
Font styles to use
Other font styles liked:
- See Website Brief file
Requirements
Must have
- Consistency in layout, colours, fonts and overall design
Should not have
- Very bright colours, hard to read fonts, unlicensed images and fonts

```html
<!DOCTYPE html>
<html lang="en">
<head>
<meta charset="utf-8">
<title>Brevka — Homepage</title>
<link href="https://fonts.googleapis.com/css2?family=Oswald:wght@400;500;600;700&family=Open+Sans:wght@400;600;700&display=swap" rel="stylesheet">
<style>
:root{
  --plum:#52225e;
  --violet:#753f9a;
  --gold:#fbbf00;
  --grey:#666666;
  --white:#ffffff;
  --canvas:#e9e9eb;
  --panel:#f4f4f6;
  --ink:#222222;
  --head:'Oswald',Impact,sans-serif;
  --body:'Open Sans',Arial,sans-serif;
}
*{box-sizing:border-box;margin:0;padding:0}
html,body{width:1200px;height:3810px;overflow:hidden}
body{background:var(--canvas);font-family:var(--body);color:var(--ink);position:relative}
.abs{position:absolute}

/* style sheet header */
.sheet-logo{left:185px;top:62px;font-family:var(--head);font-weight:700;font-size:44px;color:var(--plum);letter-spacing:.5px}
.sheet-fonts{left:502px;top:62px;color:#333}
.sheet-fonts h4{font-family:var(--body);font-weight:400;font-size:22px;margin-bottom:8px}
.sheet-fonts .f1{font-family:var(--head);font-size:20px;color:#555}
.sheet-fonts .f2{font-size:15px;color:#666}
.sheet-colors{left:795px;top:62px}
.sheet-colors h4{font-family:var(--body);font-weight:400;font-size:22px;color:#333;margin-bottom:10px}
.swatches{display:flex;gap:9px}
.swatch{width:37px;text-align:center;font-size:8px;color:#555}
.swatch i{display:block;width:37px;height:37px;border-radius:50%;margin-bottom:9px}

/* site */
.site{position:absolute;left:280px;top:217px;width:640px;height:3527px;background:var(--white);overflow:hidden}
.h{font-family:var(--head);font-weight:500;text-transform:uppercase;color:#2a2a2a;text-align:center}
.h em{font-style:normal;color:var(--plum)}
.p{font-size:7.5px;line-height:11px;color:#555}

/* nav */
.logo{left:84px;top:4px;font-family:var(--head);font-weight:700;font-size:21px;color:var(--plum)}
.topbar{left:448px;top:0;height:14px;display:flex;font-size:6px}
.topbar span{display:flex;align-items:center;padding:0 8px;background:#f0f0f0;color:#555}
.topbar .tel{background:var(--gold);color:#222;font-weight:600;width:72px;justify-content:center;gap:3px}
.menu{top:23px;font-size:5.6px;color:#444;letter-spacing:.3px}

/* hero */
.hero{left:3px;top:35px;width:634px;height:297px;border-radius:4px;background:radial-gradient(circle at 72% 45%,#9a9a9a 0,#4a4a4a 28%,#1c1c1c 60%,#111 100%)}
.hero-title{left:84px;top:145px;font-family:var(--head);font-weight:600;font-size:36px;line-height:37px;color:var(--white);text-transform:uppercase}
.hero-title b{color:var(--gold);font-weight:600}
.pick{display:inline-flex;align-items:center;justify-content:space-between;width:124px;height:28px;background:var(--white);border-radius:3px;vertical-align:middle;padding:0 7px;font-size:21px;color:var(--plum);line-height:1;margin-left:4px}

/* intro */
.intro-h{left:0;width:640px;top:368px;font-size:20px}
.intro-p{left:130px;width:380px;top:408px}
.intro-p p{margin-bottom:6px}
.intro-p .lead{color:#222}

/* grey band */
.band{left:3px;top:553px;width:634px;height:970px;background:var(--panel)}
.band-h{left:0;width:640px;top:585px;font-size:16px;line-height:21px}
.card{background:var(--white);border-radius:3px;padding:20px 14px;font-size:6.2px;line-height:8.5px;color:#888}
.card svg{display:block;margin-bottom:8px}
.card b{display:block;font-size:8px;font-weight:600;color:#333;margin-bottom:6px}
.card.hot{background:linear-gradient(120deg,var(--plum),var(--violet));color:#e8dcef}
.card.hot b{color:var(--white)}
.video{left:3px;top:951px;width:634px;height:235px;border-radius:3px;background:linear-gradient(90deg,#000 0,#080808 50%,#3a3a3a 78%,#1a1a1a 100%)}
.play{left:84px;top:1049px}
.work-h{left:0;width:640px;top:1223px;font-size:20px}
.tabs{left:0;width:640px;top:1268px;display:flex;justify-content:center;gap:22px;font-size:6.5px;color:#888}
.tabs .on{color:var(--plum)}
.slide{left:84px;top:1293px;width:472px;height:189px;border-radius:4px;background:linear-gradient(180deg,#8c8c8c 0,#5a5a5a 45%,#1f1f1f 100%)}
.slide-cap{left:84px;top:1424px;width:472px;text-align:center;color:var(--white)}
.slide-cap strong{display:block;font-weight:400;font-size:14px}
.slide-cap span{font-size:6.5px;color:#ddd}
.arrow{width:20px;height:20px;border-radius:50%;display:flex;align-items:center;justify-content:center}

/* talk */
.talk-h{left:0;width:640px;top:1556px;font-size:20px}
.talk-p{left:170px;width:300px;top:1597px;text-align:center}
.btn{display:inline-flex;align-items:center;gap:6px;height:17px;padding:0 14px;font-size:5.8px;font-weight:700;border-radius:1px}
.btn.gold{background:var(--gold);color:#222}
.btn.plum{background:var(--plum);color:var(--white)}
.or{width:26px;height:26px;border-radius:50%;background:var(--white);box-shadow:0 0 0 6px #f3f3f3;display:flex;align-items:center;justify-content:center;font-size:7px;font-weight:700}

/* numbers */
.numbers{left:3px;top:1707px;width:634px;height:229px;background:linear-gradient(100deg,var(--violet),var(--plum))}
.num-h{left:0;width:640px;top:1735px;font-size:22px;color:var(--white)}
.num-h b{color:var(--gold);font-weight:500}
.ratio{left:148px;top:1790px;font-family:var(--head);font-weight:500;font-size:118px;line-height:1;color:var(--white)}
.ratio-bar{left:301px;top:1800px;width:8px;height:90px;border-radius:4px;background:rgba(255,255,255,.18)}
.ratio-t{left:329px;top:1800px;font-size:19px;line-height:24.5px;color:var(--white)}

/* cases */
.case-h{left:0;width:640px;top:1970px;font-size:20px}
.case{width:232px;height:230px;border-radius:2px;background:linear-gradient(180deg,#d9d9d9 0,#8a8a8a 45%,#2b2b2b 85%,#1c1c1c 100%);color:var(--white);text-align:center;display:flex;flex-direction:column;justify-content:flex-end;padding-bottom:14px;font-size:6.5px;line-height:10px}
.case strong{font-family:var(--head);font-weight:500;font-size:11.5px;line-height:16px}

/* insights */
.ins{left:3px;top:2568px;width:634px;height:296px;background:var(--panel)}
.ins-h{left:0;width:640px;top:2599px;font-size:20px}
.post{width:113px;height:152px;border-radius:2px;background:linear-gradient(180deg,#bdbdbd 0,#6a6a6a 50%,#2a2a2a 100%);display:flex;align-items:flex-end;padding:6px}
.post span{display:block;width:100%;background:var(--white);font-size:6.2px;line-height:8px;text-align:center;padding:5px 3px;color:#333;border-radius:1px}
.dots{left:0;width:640px;top:2818px;display:flex;justify-content:center;gap:4px}
.dots i{width:5px;height:5px;border-radius:50%;border:1px solid #bbb}
.dots i.on{background:var(--violet);border-color:var(--violet)}

/* regions */
.reg-h{left:0;width:640px;top:2899px;font-size:20px}
.map{left:100px;top:2943px;width:440px;height:229px;background:linear-gradient(100deg,#52225e 0,#6b3a80 28%,#d3dadf 40%,#cfd6db 72%,#6b3a80 88%,#d3dadf 100%);opacity:.9;border-radius:6px}
.office{width:180px;text-align:center;font-size:6.5px;line-height:10px;color:#888}
.office b{display:block;font-family:var(--head);font-weight:500;font-size:10px;color:#333;margin-bottom:10px}
.office u{text-decoration:underline;color:#333}

/* footer */
.foot{left:3px;top:3325px;width:634px;height:202px;background:linear-gradient(100deg,var(--plum),#6a338c)}
.fcol{top:3370px;color:#d9c7e4;font-size:5.8px;line-height:15px}
.fcol h5{font-family:var(--head);font-weight:500;font-size:14px;color:var(--white);margin-bottom:6px;line-height:20px}
.fcol .w{color:var(--white);font-weight:600}
.fcol .btn{height:15px;margin-bottom:6px;display:flex;width:84px;justify-content:space-between;padding:0 8px}
.legal{left:84px;top:3509px;width:472px;display:flex;justify-content:space-between;font-size:4.8px;color:#d9c7e4}
</style>
</head>
<body>

<div class="abs sheet-logo">Brevka</div>
<div class="abs sheet-fonts"><h4>Fonts:</h4><div class="f1">OSWALD</div><div class="f2">Open Sans</div></div>
<div class="abs sheet-colors"><h4>Colors:</h4>
  <div class="swatches">
    <div class="swatch"><i style="background:var(--plum)"></i>#52225e</div>
    <div class="swatch"><i style="background:var(--violet)"></i>#753f9a</div>
    <div class="swatch"><i style="background:var(--gold)"></i>#fbbf00</div>
    <div class="swatch"><i style="background:var(--grey)"></i>#666666</div>
    <div class="swatch"><i style="background:var(--white)"></i>#ffffff</div>
  </div>
</div>

<main class="site">
  <!-- navigation -->
  <div class="abs logo">Brevka</div>
  <div class="abs topbar"><span>CONTACT US</span><span class="tel">
    <svg width="6" height="6" viewBox="0 0 24 24"><path fill="#222" d="M6.6 10.8a15 15 0 0 0 6.6 6.6l2.2-2.2c.3-.3.7-.4 1-.2 1.1.4 2.3.6 3.6.6.6 0 1 .4 1 1V20c0 .6-.4 1-1 1A17 17 0 0 1 3 4c0-.6.4-1 1-1h3.5c.6 0 1 .4 1 1 0 1.3.2 2.5.6 3.6.1.3 0 .7-.2 1z"/></svg>+44 (0) 1600 482 315</span></div>
  <div class="abs menu" style="left:327px">CLIENTS</div>
  <div class="abs menu" style="left:379px">SERVICES</div>
  <div class="abs menu" style="left:428px">CASE STUDIES</div>
  <div class="abs menu" style="left:491px">NEWS</div>
  <div class="abs menu" style="left:537px">ABOUT</div>

  <!-- hero -->
  <div class="abs hero" role="img" aria-label="Monochrome photo of a hand holding a glass globe surrounded by a network of connected people icons"></div>
  <h1 class="abs hero-title"><b>I</b>DEAL<br>ORIGINATION<br>FOR<span class="pick">YOU?<svg width="8" height="6" viewBox="0 0 8 6"><path d="M1 1l3 3 3-3" stroke="#999" fill="none"/></svg></span></h1>

  <!-- intro -->
  <h2 class="abs h intro-h">Exclusive deals, <em>reduced risk,</em> stronger leverage</h2>
  <div class="abs p intro-p">
    <p class="lead">We consistently deliver high-quality deals, bypassing the crowded open market. Imagine a pipeline filled with precise targets, aligned with your acquisition goals.</p>
    <p>Our approach minimises execution risk. We bring forward only well-matched prospects backed by transparent tracking and guidance. By specialising in off-market exclusivity, we enhance your negotiation leverage, reducing competition and securing favourable terms for both parties.</p>
    <p>We focus on quality over quantity, building high-trust seller relationships. Gain a competitive edge with our deep market knowledge and highly targeted outreach, expanding your market share. Brevka enables you to acquire smarter, faster.</p>
  </div>

  <!-- benefits band -->
  <div class="abs band"></div>
  <h2 class="abs h band-h">Brevka empowers acquirers to <em>outpace competitors</em> by<br>consistently delivering high-response, off-market<br>deal flow, without adding headcount or overhead.</h2>

  <div class="abs card" style="left:84px;top:673px;width:115px;height:112px">
    <svg width="20" height="18" viewBox="0 0 24 24" fill="none" stroke="#753f9a" stroke-width="1.3"><path d="M4 8h4a2 2 0 1 1 4 0h4v4a2 2 0 1 1 0 4v4H4v-4a2 2 0 1 0 0-4z"/></svg>
    <b>Find the ideal fit</b>Target businesses that match your exact criteria</div>
  <div class="abs card" style="left:204px;top:673px;width:112px;height:112px">
    <svg width="20" height="18" viewBox="0 0 24 24" fill="none" stroke="#753f9a" stroke-width="1.3"><circle cx="12" cy="12" r="3"/><path d="M12 2v4M12 18v4M2 12h4M18 12h4M5 5l3 3M16 16l3 3M5 19l3-3M16 8l3-3"/></svg>
    <b>More options</b>Access businesses that aren't publicly listed</div>
  <div class="abs card hot" style="left:324px;top:673px;width:232px;height:112px">
    <svg width="20" height="18" viewBox="0 0 24 24" fill="none" stroke="#fff" stroke-width="1.3"><path d="M3 9h4l6-4v14l-6-4H3z"/><path d="M17 10l4 4M21 10l-4 4"/></svg>
    <b>No noise</b>Avoid any unnecessary disruption from the advisors<br>and brokers</div>
  <div class="abs card" style="left:84px;top:794px;width:232px;height:111px">
    <svg width="22" height="18" viewBox="0 0 24 24" fill="none" stroke="#753f9a" stroke-width="1.3"><path d="M2 9l5-4 5 3 5-3 5 4-5 6-4 3-6-5z"/></svg>
    <b>Higher-quality deals</b>Engage directly with owners who prefer a discreet and<br>low-profile sale</div>
  <div class="abs card" style="left:324px;top:794px;width:112px;height:111px">
    <svg width="20" height="18" viewBox="0 0 24 24" fill="none" stroke="#753f9a" stroke-width="1.3"><rect x="4" y="3" width="13" height="17" rx="1"/><path d="M7 8h7M7 12h7M7 16h4"/><circle cx="18" cy="17" r="3"/></svg>
    <b>More control</b>Move at your own pace, without broker pressure</div>
  <div class="abs card" style="left:444px;top:794px;width:112px;height:111px">
    <svg width="20" height="18" viewBox="0 0 24 24" fill="none" stroke="#753f9a" stroke-width="1.3"><circle cx="8" cy="7" r="3"/><path d="M2 20c0-4 3-6 6-6s6 2 6 6"/><rect x="14" y="11" width="8" height="7" rx="1"/></svg>
    <b>Strong relationship</b>Direct contact with business owners</div>

  <div class="abs video" role="img" aria-label="Dark video still of a padlock set into a black leather case"></div>
  <svg class="abs play" width="40" height="40" viewBox="0 0 40 40"><circle cx="20" cy="20" r="19" fill="#fbbf00" stroke="#7a5c00" stroke-width="1.5"/><path d="M16 13l11 7-11 7z" fill="#fff"/></svg>

  <h2 class="abs h work-h">We <em>work</em> for</h2>
  <div class="abs tabs"><span class="on">Private Equity</span><span>Trade Buyers</span><span>Sellers</span><span>MBI Candidates</span><span>Corporate Finance</span><span>Search Funds</span></div>
  <div class="abs slide" role="img" aria-label="Black and white photo of business professionals meeting in an office"></div>
  <div class="abs slide-cap"><strong>Private Equity</strong><span>Expand your pipeline beyond traditional brokers and geographic boundaries.</span></div>
  <div class="abs arrow" style="left:74px;top:1378px;background:#f3f3f3"><svg width="6" height="8" viewBox="0 0 6 8"><path d="M5 1L2 4l3 3" stroke="#fbbf00" fill="none" stroke-width="1.3"/></svg></div>
  <div class="abs arrow" style="left:546px;top:1378px;background:var(--violet)"><svg width="6" height="8" viewBox="0 0 6 8"><path d="M1 1l3 3-3 3" stroke="#fff" fill="none" stroke-width="1.3"/></svg></div>

  <!-- talk -->
  <h2 class="abs h talk-h">If you want <em>ideal flow,</em> let's talk</h2>
  <p class="abs p talk-p">There is only so much you can tell from reviewing our website, the best way to explore is to have a short meeting with one of our team.</p>
  <div class="abs" style="left:226px;top:1640px;display:flex;align-items:center;gap:4px">
    <span class="btn gold">Contact Brevka <span>›</span></span><span class="or">or</span><span class="btn plum">Book Appointment <span>›</span></span>
  </div>

  <!-- numbers -->
  <div class="abs numbers"></div>
  <h2 class="abs h num-h"><b>Brevka</b> the numbers</h2>
  <div class="abs ratio">1:5</div>
  <div class="abs ratio-bar"></div>
  <p class="abs ratio-t">For every 1<br>target approached,<br>we analyse at least<br>5 companies!</p>

  <!-- case studies -->
  <h2 class="abs h case-h">Recent <em>case</em> studies</h2>
  <div class="abs case" style="left:84px;top:2016px" role="img" aria-label="Monochrome photo of an open door with a handshake">Leading Labour Recruitment Company<strong>ACQUIRED</strong>An Established Construction &amp; Recruitment Firm</div>
  <div class="abs case" style="left:324px;top:2016px" role="img" aria-label="Monochrome photo of an open safe door">Fire Safety Focused Investment Group<strong>ACQUIRED</strong>A Bespoke Fire and Security Solutions Business</div>
  <div class="abs case" style="left:84px;top:2255px" role="img" aria-label="Monochrome photo of an open safe door">Fire Safety Focused Investment Group<strong>ACQUIRED</strong>A Bespoke Fire and Security Solutions Business</div>
  <div class="abs case" style="left:324px;top:2255px" role="img" aria-label="Monochrome photo of an open door with a handshake">Leading Labour Recruitment Company<strong>ACQUIRED</strong>An Established Construction &amp; Recruitment Firm</div>
  <div class="abs" style="left:277px;top:2509px"><span class="btn gold">More Case Studies <span>›</span></span></div>

  <!-- insights -->
  <div class="abs ins"></div>
  <h2 class="abs h ins-h">M&amp;A <em>insights</em> and latest trends</h2>
  <div class="abs post" style="left:84px;top:2650px" role="img" aria-label="Chess piece on a connected network board"><span>Why the Off Market is Key for the Motivated Buyer</span></div>
  <div class="abs post" style="left:203px;top:2650px" role="img" aria-label="Hands signing a document at a desk"><span>How to Finance Your Next Business Acquisition?</span></div>
  <div class="abs post" style="left:322px;top:2650px" role="img" aria-label="City skyline with network points"><span>Is There Suitable Business for Sale Near Me?</span></div>
  <div class="abs post" style="left:441px;top:2650px" role="img" aria-label="Hand holding a pen over a financial chart"><span>How to Finance Your Next Business Acquisition?</span></div>
  <div class="abs dots"><i></i><i class="on"></i><i></i></div>

  <!-- regions -->
  <h2 class="abs h reg-h">Regional and <em>cross-border</em> deal makers</h2>
  <div class="abs map" role="img" aria-label="World map highlighting North America, UK and Europe, India and Australia in purple"></div>
  <div class="abs office" style="left:106px;top:3205px"><b>UK &amp; Europe Office</b>Second Floor Kestrel House<br>Halden<br>HX4 2LT<br><br>Contact<br><u>+44 (0) 1600 482 315</u></div>
  <div class="abs office" style="left:351px;top:3205px"><b>APAC Office</b>8 Marlow Lane<br>Westhaven NSW 2190<br>Australia<br><br>Contact<br><u>+61 (0) 400 218 667</u></div>

  <!-- footer -->
  <div class="abs foot"></div>
  <div class="abs fcol" style="left:84px"><h5>Clients</h5>Private Equity<br>Trade Buyers<br>Management Buy-In<br>Search Funds<br>Corporate Finance</div>
  <div class="abs fcol" style="left:229px"><h5>Services</h5>Deal Origination<br>Single Acquisitions<br>Buy and Build<br>Bolt-On Acquisitions<br>Cross Border / International</div>
  <div class="abs fcol" style="left:333px;top:3396px">Acquisition Finance<br>Negotiation Support<br>Due Diligence</div>
  <div class="abs fcol" style="left:481px"><h5>Contact</h5><div class="w">+44 (0) 1600 482 315</div><div style="height:12px"></div><span class="btn gold">Contact Brevka <span>›</span></span><span class="btn plum" style="background:#3f1849">Book Appointment <span>›</span></span></div>
  <div class="abs legal"><span>© Brevka All Rights Reserved</span><span>Policies &nbsp;|&nbsp; Terms of Use &nbsp;|&nbsp; Privacy Policy &nbsp;|&nbsp; Contact Us</span></div>
</main>

</body>
</html>
```